A5 flyer required for 3D printing company

We are a 3D printing company providing our customers with customised 3D printed figurines services. And we need a double sided flyer design for our company, either to display in the shop or hand out on streets. Our website (www.tivolafigs.com.au) describes what we do and what the products look like.
The final flyer should tell our potential customers the following points:
1. We can make 3D printed figurines in incredible likeness for our customers;
2. Advanced 3D scanning and 3D printing technology;
3. Includes our price table, and grand opening 15% off for all products till 31st May 2016;
full body size Retail
8cm $159
10cm $239
12cm $279
15cm $339
18cm $449
20cm $599
Bust size
8cm $239
10cm $279
12cm $339
4. Use one or more photos supplied to show the final products compared with real person, you can use lasso tools to crop the background if you like;
5. Our contact details;
Address: Suite 7 Level 3, 516 Harlow Street Sydney, in the Brennick Building
Telephone: 02 9487 5326
Email: info@tivolafigs.com.au
Web: www.tivolafigs.com.au
The flyer should catch customers' eyes at the first sight because we will be handing out the flyers on streets as well. You can use any material used on our website (www.tivolafigs.com.au).
We would like to see the design in line with our colour scheme used for our logo. The two colours used in the logo are C70 M0 Y0 K0 and C83 M53 Y6 K0 for your reference. And the font we used in our logo is hobo std for your reference.
If you have any questions about our products or the flyer, please feel free to drop us a message.

```html
<!DOCTYPE html>
<html lang="en">
<head>
<meta charset="utf-8">
<title>Tivola Figs – The Future of Photography</title>
<link rel="stylesheet" href="https://fonts.googleapis.com/css2?family=Barlow:wght@300;400;500;600;700;800&display=swap">
<style>
  :root{
    --sky:#2bb5e8;
    --azure:#1c96d8;
    --navy:#1a64ad;
    --deep:#1457a0;
    --ink:#1d1d1b;
    --white:#ffffff;
    --orange-core:#f36f12;
    --orange-rim:#f9a51a;
  }
  *{margin:0;padding:0;box-sizing:border-box}
  html,body{width:934px;height:1200px;overflow:hidden;background:#fff}
  body{font-family:"Barlow",Arial,sans-serif;color:var(--ink)}
  .flyer{position:relative;width:934px;height:1200px;overflow:hidden;background:var(--white)}

  .hero-photo{position:absolute;left:0;top:0;width:934px;height:490px;
    background:
      radial-gradient(ellipse 260px 150px at 610px 400px,rgba(246,242,228,.95) 0%,rgba(236,230,212,.6) 50%,rgba(236,230,212,0) 100%),
      radial-gradient(ellipse 220px 170px at 470px 170px,rgba(214,170,135,.55) 0%,rgba(214,170,135,0) 100%),
      radial-gradient(ellipse 180px 110px at 440px 40px,rgba(40,34,30,.55) 0%,rgba(40,34,30,0) 100%),
      radial-gradient(ellipse 320px 60px at 180px 95px,rgba(255,255,255,.75) 0%,rgba(255,255,255,0) 100%),
      radial-gradient(ellipse 260px 50px at 850px 110px,rgba(255,255,255,.7) 0%,rgba(255,255,255,0) 100%),
      linear-gradient(180deg,#6fa3d6 0%,#9cc2e2 16%,#d9e6ee 30%,#b3b6a8 38%,#8c806c 52%,#7b7a62 68%,#6a6e5c 84%,#5c6257 100%);}

  .shapes{position:absolute;left:0;top:0;width:934px;height:1200px}
  .web{position:absolute;right:30px;top:24px;font-size:13px;font-weight:400;color:var(--white);letter-spacing:.3px}

  .badge{position:absolute;left:58px;top:442px;width:280px;height:280px;border-radius:50%;
    background:radial-gradient(circle at 50% 50%,var(--orange-core) 0%,#f47f15 60%,var(--orange-rim) 100%);
    box-shadow:0 5px 10px rgba(0,0,0,.18)}
  .badge-num{position:absolute;left:52px;top:50px;font-size:120px;font-weight:800;line-height:1;color:#111;letter-spacing:-5px}
  .badge-pct{position:absolute;left:172px;top:60px;font-size:58px;font-weight:800;line-height:1;color:#111}
  .badge-off{position:absolute;left:174px;top:124px;font-size:32px;font-weight:800;line-height:1;color:#111}
  .badge-note{position:absolute;left:0;top:162px;width:280px;text-align:center;font-size:20px;font-weight:400;line-height:25px;color:#2a1a0a;letter-spacing:.3px}

  .headline{position:absolute;right:132px;top:506px;text-align:right;color:var(--white)}
  .headline-top{font-size:46px;font-weight:300;line-height:52px;letter-spacing:1.5px}
  .headline-main{font-size:61px;font-weight:700;line-height:64px;letter-spacing:1.5px}
  .headline-lede{margin-top:12px;font-size:20px;font-weight:300;line-height:25px;letter-spacing:.3px}

  .about{position:absolute;left:73px;top:738px;width:410px}
  .about-title{font-size:24px;font-weight:700;color:var(--navy);line-height:28px;margin-bottom:10px}
  .about p{font-size:13.6px;line-height:17.6px;margin-bottom:8px;letter-spacing:.15px}

  .product-photo{position:absolute;top:929px;width:210px;height:145px;border-radius:6px;box-shadow:0 3px 8px rgba(0,0,0,.3)}
  .product-photo.full{left:73px;background:linear-gradient(180deg,#a9c3e2 0%,#d7cfb3 24%,#bfae86 32%,#6fa04a 40%,#4f8a34 100%)}
  .product-photo.bust{left:310px;background:linear-gradient(180deg,#d6d9dc 0%,#bfc2c5 55%,#8e9194 100%)}

  .prices{position:absolute;top:1088px;color:var(--white);font-size:14px;line-height:18px}
  .prices h3{font-size:14px;font-weight:600;margin-bottom:1px}
  .prices table{border-collapse:collapse}
  .prices td{padding:0;font-weight:400}
  .prices.full{left:73px}
  .prices.bust{left:334px}
  .prices.full td:nth-child(1){width:53px}
  .prices.full td:nth-child(2){width:61px}
  .prices.full td:nth-child(3){width:53px}
  .prices.bust td:nth-child(1){width:53px}

  .brand{position:absolute;left:676px;top:970px;width:212px;text-align:center;font-size:42px;font-weight:700;color:var(--azure);line-height:1}
  .contact{position:absolute;left:680px;top:1068px;color:var(--navy);font-style:normal}
  .phone{display:flex;align-items:center;gap:4px;font-size:31px;font-weight:700;line-height:1}
  .contact-line{display:flex;align-items:flex-start;gap:6px;font-size:13.5px;line-height:18px;margin-left:3px}
  .contact-line:first-of-type{margin-top:6px}
  .contact-line svg{flex:none;margin-top:4px}
  .address{margin-left:21px;font-size:13.5px;line-height:18px}
</style>
</head>
<body>
<main class="flyer">
  <div class="hero-photo" role="img" aria-label="Photo of a young man on a rooftop above a sunny city skyline, holding a small 3D printed figurine of himself"></div>

  <svg class="shapes" viewBox="0 0 1167 1500" width="934" height="1200" aria-hidden="true">
    <defs>
      <linearGradient id="bandBottom" x1="0" y1="0" x2="0" y2="1">
        <stop offset="0" stop-color="#2bb5e8"/>
        <stop offset="1" stop-color="#1a78c2"/>
      </linearGradient>
    </defs>
    <polygon points="540,0 1167,0 1167,20 1090,115" fill="#1a64ad"/>
    <polygon points="720,0 1167,0 1167,88 1110,80" fill="#2bb5e8"/>
    <polygon points="0,430 200,462 1167,605 1167,612 0,612" fill="#2bb5e8" opacity=".35"/>
    <polygon points="0,585 95,510 1167,604 985,1098 380,830 0,800" fill="#2bb5e8"/>
    <polygon points="0,560 95,510 30,760 0,800" fill="#1c96d8"/>
    <polygon points="1100,600 1167,580 1167,1015 985,1098" fill="#1a64ad"/>
    <polygon points="0,1285 780,1213 700,1500 0,1500" fill="url(#bandBottom)"/>
    <polygon points="700,1500 780,1213 735,1500" fill="#1a64ad"/>
  </svg>

  <div class="web">www.tivolafigs.com.au</div>

  <div class="badge">
    <span class="badge-num">15</span>
    <span class="badge-pct">%</span>
    <span class="badge-off">OFF</span>
    <p class="badge-note">for all products<br>till 31st May 2016</p>
  </div>

  <header class="headline">
    <div class="headline-top">THE FUTURE OF</div>
    <h1 class="headline-main">PHOTOGRAPHY</h1>
    <p class="headline-lede">Take a 3D printed&nbsp; figurine to<br>last a lifetime! Discover the<br>magic of 3D photos and bring to<br>life your memories!</p>
  </header>

  <section class="about">
    <h2 class="about-title">Discover Tivola Figs</h2>
    <p>Tivola Figs was born from the desire to bring memories to life. They offer people the amazing opportunity to relive the most beautiful moments in their lives. We use the most detailed and fast technology capable of collecting 3D data and process it into superb miniature figurines of...you.</p>
    <p>We use Prismatec ColorForge printers, the only 3D printers on the market that manage to create 3D prints of outstanding quality.</p>
  </section>

  <div class="product-photo full" role="img" aria-label="Full body 3D printed figurine of a man with a camera standing on a lawn before a historic crescent building"></div>
  <div class="product-photo bust" role="img" aria-label="3D printed figurines of an elderly couple with a young girl"></div>

  <section class="prices full">
    <h3>Full body size</h3>
    <table>
      <tr><td>8cm</td><td>$159</td><td>15cm</td><td>$339</td></tr>
      <tr><td>10cm</td><td>$239</td><td>18cm</td><td>$449</td></tr>
      <tr><td>12cm</td><td>$279</td><td>20cm</td><td>$599</td></tr>
    </table>
  </section>

  <section class="prices bust">
    <h3>Bust size</h3>
    <table>
      <tr><td>8cm</td><td>$239</td></tr>
      <tr><td>10cm</td><td>$279</td></tr>
      <tr><td>12cm</td><td>$339</td></tr>
    </table>
  </section>

  <div class="brand">Tivola Figs</div>

  <address class="contact">
    <div class="phone">
      <svg width="22" height="22" viewBox="0 0 24 24" aria-hidden="true"><path d="M6.6 10.8a15.1 15.1 0 0 0 6.6 6.6l2.2-2.2a1 1 0 0 1 1-.25 11.4 11.4 0 0 0 3.6.57 1 1 0 0 1 1 1V20a1 1 0 0 1-1 1A17 17 0 0 1 3 4a1 1 0 0 1 1-1h3.5a1 1 0 0 1 1 1c0 1.25.2 2.45.57 3.570a1 1 0 0 1-.25 1z" fill="#1c96d8"/></svg>
      <span>02 9487 5326</span>
    </div>
    <div class="contact-line">
      <svg width="12" height="10" viewBox="0 0 12 10" aria-hidden="true"><rect x=".6" y=".6" width="10.8" height="8.8" fill="none" stroke="#1c96d8" stroke-width="1.2"/><path d="M.6 .6 6 5.2 11.4 .6" fill="none" stroke="#1c96d8" stroke-width="1.2"/></svg>
      <span>info@tivolafigs.com.au</span>
    </div>
    <div class="contact-line">
      <svg width="11" height="14" viewBox="0 0 11 14" aria-hidden="true"><path d="M5.5 0A5.5 5.5 0 0 0 0 5.5C0 9.6 5.5 14 5.5 14S11 9.6 11 5.5A5.5 5.5 0 0 0 5.5 0z" fill="#1c96d8"/><circle cx="5.5" cy="5.3" r="2" fill="#fff"/></svg>
      <span>Suite 7 Level 3,</span>
    </div>
    <div class="address">516 Harlow Street Sydney<br>(in the Brennick Building)</div>
  </address>
</main>
</body>
</html>
```